Vextara website

Web design for small consulting firm
It can be simple, easy to find approach

The primary use is business to business for

a. people wanting to find out a bit more of us after receiving a business card
b. Search words to draw people from search engines to us

Target Market(s)

Senior staff of large companies, in their work capacity
MD / CEO / CFO , directors, etc.

Industry/Entity Type

Business

Colors
ffffff
f79020
faa54b
33a6d7

```html
<!DOCTYPE html>
<html lang="en">
<head>
<meta charset="utf-8">
<title>Vextara Insight</title>
<link href="https://fonts.googleapis.com/css2?family=Questrial&family=Mulish:wght@400;600;700&display=swap" rel="stylesheet">
<style>
:root{
  --orange:#f79020;
  --orange-light:#faa54b;
  --blue:#0f6fb8;
  --blue-bright:#33a6d7;
  --blue-dark:#0b5c9c;
  --ink:#555a60;
  --footer:#3a3a3a;
  --footer-line:#555;
  --band:#ececee;
  --white:#ffffff;
}
*{margin:0;padding:0;box-sizing:border-box}
html,body{width:816px;height:1200px;overflow:hidden;background:var(--white)}
body{position:relative;font-family:"Mulish",sans-serif;color:var(--ink)}
h1,h2,h3,h4{font-weight:400}
.abs{position:absolute}

/* header */
.site-header{left:0;top:0;width:816px;height:130px;border-top:2px solid var(--orange);
  background:linear-gradient(#fafafa,#ececec);border-bottom:1px solid #d4d4d4}
.brand{left:68px;top:56px;font-family:"Questrial",sans-serif;color:var(--blue);font-size:24px;line-height:1;display:flex;align-items:center;gap:7px}
.brand-mark{width:11px;height:11px;border-radius:50%;background:var(--blue)}
.main-nav{left:197px;top:61px;display:flex;align-items:center;font-family:"Questrial",sans-serif;font-size:10px;letter-spacing:.8px;color:#444}
.main-nav a{color:inherit;text-decoration:none;padding:4px 13px;margin-right:1px}
.main-nav a.active{background:var(--blue);color:var(--white);border-radius:10px;padding:5px 13px}
.social{display:flex;gap:7px}
.social span{width:19px;height:19px;border-radius:50%;background:var(--blue);display:block}
.social-top{left:665px;top:25px}

/* hero */
.hero{left:0;top:131px;width:816px;height:343px;background:linear-gradient(#f7f7f7,#e6e6e8)}
.hero-title{left:80px;top:174px;font-family:"Questrial",sans-serif;font-size:18px;letter-spacing:1px;color:var(--blue)}
.hero-text{left:80px;top:204px;width:270px;font-size:11px;line-height:17.6px;letter-spacing:.3px;color:var(--ink)}
.hero-text p+p{margin-top:17.6px}
.btn{display:flex;align-items:center;justify-content:center;color:var(--white);font-size:9px;letter-spacing:.6px;font-weight:400}
.btn-read{left:80px;top:361px;width:90px;height:25px;background:var(--orange)}
.btn-contact{left:181px;top:361px;width:90px;height:25px;background:var(--blue)}
.hero-media{left:420px;top:180px;width:299px;height:242px;border-radius:4px;
  background:linear-gradient(#2a2a2a 0 70%,#cfd1d3 70% 86%,#e6e7e8 86%)}
.hero-media::after{content:"";position:absolute;left:13px;top:10px;width:273px;height:158px;
  background:linear-gradient(135deg,#c9d4dc,#e8e2da 45%,#7a8898)}

/* featured */
.featured-bar{left:54px;top:440px;width:707px;height:34px;background:linear-gradient(var(--blue-bright),var(--blue) 55%,var(--blue-dark));border-radius:3px 3px 0 0}
.featured-title{left:93px;top:449px;font-family:"Questrial",sans-serif;font-size:15px;letter-spacing:1.2px;color:var(--white)}
.search{left:617px;top:447px;width:136px;height:19px;border-radius:10px;background:var(--white);font-size:9px;color:#888;padding:4px 9px;letter-spacing:.4px}
.search svg{position:absolute;right:8px;top:5px}
.featured-panel{left:54px;top:474px;width:707px;height:362px;background:var(--white);box-shadow:0 3px 10px rgba(0,0,0,.25)}
.card-img{width:165px;height:110px;border:2px solid #dcdcdc}
.card-title{font-family:"Questrial",sans-serif;font-size:12.5px;letter-spacing:.8px;color:var(--blue);line-height:12px}
.card-text{width:162px;font-size:9.6px;line-height:12.8px;letter-spacing:.5px;color:var(--ink)}
.ticks{list-style:none;margin-top:3px}
.ticks li{display:flex;align-items:center;gap:5px;line-height:12.8px}
.ticks li::before{content:"";width:8px;height:8px;border-radius:50%;background:var(--blue-bright)}
.btn-more{width:84px;height:19px;background:var(--orange);font-size:8px;box-shadow:2px 2px 2px rgba(0,0,0,.15)}

/* clients */
.clients{left:0;top:836px;width:816px;height:101px;background:var(--band)}
.client{top:880px;font-family:"Questrial",sans-serif;font-size:13px;color:#777;letter-spacing:.6px}
.client-badge{left:378px;top:862px;width:50px;height:50px;border-radius:50%;background:#cfcfcf}

/* footer */
.site-footer{left:0;top:937px;width:816px;height:234px;background:var(--footer)}
.foot-h{top:965px;font-family:"Questrial",sans-serif;font-size:14.5px;letter-spacing:1.2px;color:var(--white)}
.rule{height:1px;background:var(--footer-line)}
.thumb{width:54px;height:51px;border:2px solid #888;background:linear-gradient(135deg,#c8d0d8,#7f8ea0)}
.article{left:144px;width:190px;font-size:9px;line-height:11.3px;letter-spacing:.3px;color:#ddd}
.article b{font-weight:400;color:var(--white);letter-spacing:.8px}
.quick{left:380px;top:1003px;list-style:none;font-size:9px;letter-spacing:.4px;color:#e5e5e5}
.quick li{line-height:16.4px;display:flex;align-items:center;gap:6px}
.quick li::before{content:"→";font-size:8px;color:#ccc}
.loc{left:552px;font-size:9px;letter-spacing:.6px;line-height:14.4px;color:#e5e5e5;display:flex;gap:6px}
.loc svg{flex:none;margin-top:2px}
.bottom-bar{left:0;top:1171px;width:816px;height:29px;background:var(--blue)}
.copyright{left:78px;top:1181px;font-size:8px;letter-spacing:.5px;color:var(--white)}
.social-foot{left:659px;top:1176px}
.social-foot span{width:15px;height:15px;background:var(--white)}
</style>
</head>
<body>

<header class="abs site-header"></header>
<div class="abs brand"><span class="brand-mark"></span>Vextara</div>
<nav class="abs main-nav">
  <a class="active">HOME</a><a>ABOUT</a><a>OUR VALUES</a><a>SERVICES ▾</a><a>CLIENTS</a><a>BLOG</a><a>USEFUL LINKS</a><a>CONTACT</a>
</nav>
<div class="abs social social-top"><span></span><span></span><span></span><span></span></div>

<section class="abs hero"></section>
<h1 class="abs hero-title">Vextara Insight</h1>
<div class="abs hero-text">
  <p>Lorem ipsum dolor sit amet, consectetur adipi-scing elit. Phasellus eget leo leo. Sed adipiscing mi orci, vel ultrices turpis mattis a. Quisque sed eros luctus, euismod ligula et, suscipit dolor.</p>
  <p>Sed suscipit tortor eget leo hendrerit semper. Sed adipiscing mi orci, vel ultrices turpis mattis. Quisque sed eros luctus euismod ligula.</p>
</div>
<div class="abs btn btn-read">READ MORE</div>
<div class="abs btn btn-contact">CONTAC US</div>
<div class="abs hero-media" role="img" aria-label="Desktop monitor showing colleagues in a business meeting"></div>

<div class="abs featured-panel"></div>
<div class="abs featured-bar"></div>
<h2 class="abs featured-title">FEATURED SERVICES</h2>
<div class="abs search">Keyword Search...
  <svg width="10" height="10" viewBox="0 0 10 10"><circle cx="4" cy="4" r="3" fill="none" stroke="#888" stroke-width="1.3"/><line x1="6.2" y1="6.2" x2="9" y2="9" stroke="#888" stroke-width="1.5"/></svg>
</div>

<div class="abs card-img" style="left:102px;top:516px;background:linear-gradient(#cfd8e0,#8d96a0 60%,#b58a62)" role="img" aria-label="Two professionals in discussion across a table"></div>
<h3 class="abs card-title" style="left:104px;top:640px">Governance</h3>
<div class="abs card-text" style="left:104px;top:660px">One-on-one sessions between a coach and an executive to gain a vision and develop leadership skills. Process includes:
  <ul class="ticks"><li>Needs Assessment</li><li>Coaching Plan</li><li>360 Degree Feedback</li></ul>
</div>
<div class="abs btn btn-more" style="left:104px;top:780px">more details</div>

<div class="abs card-img" style="left:324px;top:516px;background:linear-gradient(135deg,#f4f4f4,#d8d8d8 50%,#8a8a8a)" role="img" aria-label="Businesswoman beside a rising bar chart"></div>
<h3 class="abs card-title" style="left:326px;top:634px">Mentoring Business<br>&amp; Advice</h3>
<div class="abs card-text" style="left:326px;top:660px">Lorem ipsum dolor sit amet, consectetur adipiscing elit. Ut consectetur varius lacus, non rhoncus turpis pharetra et. Ut ut euismod magna. Proin non nibh dignissim, volutpat elit ut, cursus dolor.</div>
<div class="abs btn btn-more" style="left:326px;top:780px">more details</div>

<div class="abs card-img" style="left:544px;top:516px;background:linear-gradient(135deg,#2f6fc4,#8cc4ee 55%,#3a7fd0)" role="img" aria-label="Hands working with a calculator and documents"></div>
<h3 class="abs card-title" style="left:546px;top:634px">Financial<br>Management Insight</h3>
<div class="abs card-text" style="left:546px;top:660px">Lorem ipsum dolor sit amet, consectetur adipiscing elit. Ut consectetur varius lacus, non rhoncus turpis pharetra et. Ut ut euismod magna. Proin non nibh dignissim, volutpat elit ut, cursus dolor.</div>
<div class="abs btn btn-more" style="left:548px;top:780px">more details</div>

<section class="abs clients"></section>
<div class="abs client" style="left:112px">CORVANE</div>
<div class="abs client" style="left:238px">Halbrook Trust</div>
<div class="abs client-badge" role="img" aria-label="Partner badge"></div>
<div class="abs client" style="left:482px">Meridex</div>
<div class="abs client" style="left:614px">NORWELL AMES</div>

<footer class="abs site-footer"></footer>
<h4 class="abs foot-h" style="left:74px">ARTICLES &amp; PUBLICATIONS</h4>
<div class="abs rule" style="left:75px;top:991px;width:260px"></div>
<div class="abs thumb" style="left:77px;top:1004px" role="img" aria-label="Calculator keypad"></div>
<div class="abs article" style="top:1006px"><b>TITLE OF THE ARTICLE HERE</b><br>Lorem ipsum dolor sit amet consectetur adipiscing elit. Ut consectetur varius lacus, non rhoncus turpis pharetra et.</div>
<div class="abs rule" style="left:75px;top:1068px;width:260px"></div>
<div class="abs thumb" style="left:77px;top:1082px" role="img" aria-label="Calculator keypad"></div>
<div class="abs article" style="top:1083px"><b>TITLE OF THE ARTICLE HERE</b><br>Lorem ipsum dolor sit amet consectetur adipiscing elit. Ut consectetur varius lacus, non rhoncus turpis pharetra et.</div>
<div class="abs rule" style="left:75px;top:1147px;width:260px"></div>

<h4 class="abs foot-h" style="left:375px">QUICKLINKS</h4>
<div class="abs rule" style="left:377px;top:991px;width:119px"></div>
<ul class="abs quick"><li>Home</li><li>About</li><li>Our Values</li><li>Services</li><li>Clients</li><li>Blog</li><li>Useful Lnks</li><li>Contact</li></ul>
<div class="abs rule" style="left:377px;top:1147px;width:119px"></div>

<h4 class="abs foot-h" style="left:542px">OUR LOCATION</h4>
<div class="abs rule" style="left:543px;top:991px;width:192px"></div>
<div class="abs loc" style="top:1002px"><svg width="9" height="12" viewBox="0 0 9 12"><path d="M4.5 0A4.5 4.5 0 0 0 0 4.5C0 8 4.5 12 4.5 12S9 8 9 4.5A4.5 4.5 0 0 0 4.5 0z" fill="#ccc"/><circle cx="4.5" cy="4.5" r="1.7" fill="#3a3a3a"/></svg><span>Lorem Ipsum office<br>14 Harbor Point Way<br>Lakeview, FL 30210</span></div>
<div class="abs loc" style="top:1050px"><svg width="10" height="8" viewBox="0 0 10 8"><path d="M0 3C0 0 10 0 10 3L8 3.5 7 2H3L2 3.5z M2 4h6l1 4H1z" fill="#ccc"/></svg><span>+100 555 0142</span></div>
<div class="abs loc" style="top:1070px"><svg width="10" height="7" viewBox="0 0 10 7"><rect width="10" height="7" fill="#ccc"/><path d="M0 0l5 4 5-4" fill="none" stroke="#3a3a3a" stroke-width="1"/></svg><span>hello@vextara-mail.com</span></div>
<div class="abs rule" style="left:543px;top:1147px;width:192px"></div>

<div class="abs bottom-bar"></div>
<div class="abs copyright">© 2014 Vextara Insight All rights reserved.</div>
<div class="abs social social-foot"><span></span><span></span><span></span><span></span></div>

</body>
</html>
```